dorwial business card design so that it looks better

need a new business card designed. use our website, dorwian.com for example. I attached an example of a previous card we had and liked. this is for law enforcement and we have attached a previous business card as an example. This site forces me to select color and font, ignore those as I picked stuff just to get this completed.

Target Market(s)

law enforcement, local government

Contact Information for Business Card

see the attached example and our website

Font styles to use
Serif

```html
<!DOCTYPE html>
<html lang="en">
<head>
<meta charset="UTF-8">
<title>Dorwial Business Card</title>
<link href="https://fonts.googleapis.com/css2?family=Lato:wght@300;400;700;900&display=swap" rel="stylesheet">
<style>
  :root {
    --backdrop: #e4e4e6;
    --card: #0f1b25;
    --ink: #ffffff;
    --ink-soft: #c9cfd4;
  }
  * { margin: 0; padding: 0; box-sizing: border-box; }
  html, body {
    width: 1200px; height: 900px; overflow: hidden;
    background: var(--backdrop);
    font-family: "Lato", Arial, sans-serif;
    color: var(--ink);
  }
  .stage {
    position: relative; width: 1200px; height: 900px;
  }
  .card {
    position: absolute;
    width: 525px; height: 300px;
    background: var(--card);
    border-radius: 26px;
    box-shadow: 0 10px 24px rgba(0,0,0,0.22);
  }
  .card--front { left: 338px; top: 115px; }
  .card--back { left: 338px; top: 470px; }

  .wordmark {
    font-weight: 300;
    letter-spacing: 0.18em;
    color: var(--ink);
    white-space: nowrap;
  }
  .card--front .wordmark {
    position: absolute; left: 0; right: 0; top: 92px;
    text-align: center; font-size: 50px;
  }
  .tagline {
    position: absolute; left: 0; right: 0; top: 214px;
    text-align: center;
    font-size: 13px; font-weight: 700; letter-spacing: 0.04em;
    text-transform: uppercase;
  }

  .card--back .wordmark {
    position: absolute; left: 36px; top: 70px;
    font-size: 46px;
  }
  .address {
    position: absolute; right: 34px; top: 36px;
    text-align: right; font-size: 15px; line-height: 1.3;
    color: var(--ink-soft);
  }
  .person {
    position: absolute; left: 40px; top: 160px;
  }
  .person__name {
    font-size: 17px; font-weight: 900; letter-spacing: 0.03em;
    text-transform: uppercase; line-height: 1.05;
  }
  .person__role {
    font-size: 15px; color: var(--ink-soft); line-height: 1.15;
  }
  .contact-list {
    list-style: none; margin-top: 10px;
  }
  .contact-list li {
    display: flex; align-items: center; gap: 8px;
    font-size: 15px; line-height: 1.35; color: var(--ink-soft);
  }
  .contact-list svg { width: 12px; height: 12px; fill: var(--ink); flex: none; }
</style>
</head>
<body>
<main class="stage">
  <section class="card card--front">
    <div class="wordmark">DORWIAL</div>
    <p class="tagline">Law Enforcement Innovation</p>
  </section>

  <section class="card card--back">
    <div class="wordmark">DORWIAL</div>
    <address class="address" style="font-style:normal">
      4120 Larkspur Avenue<br>Fairview, TX 75069
    </address>
    <div class="person">
      <p class="person__name">Marcus Hale</p>
      <p class="person__role">Managing Director</p>
      <ul class="contact-list">
        <li>
          <svg viewBox="0 0 12 12" aria-hidden="true"><path d="M1 4c0-2 2-3 5-3s5 1 5 3v1H8.5V4h-5v1H1zM2.5 6h7l1 5h-9z"/></svg>
          866.555.0142
        </li>
        <li>
          <svg viewBox="0 0 12 12" aria-hidden="true"><path d="M0 2h12v8H0zM1 3v.4l5 3.3 5-3.3V3z" fill-rule="evenodd"/></svg>
          info@dorwian.com
        </li>
        <li>
          <svg viewBox="0 0 12 12" aria-hidden="true"><circle cx="6" cy="6" r="5.5"/></svg>
          www.dorwian.com
        </li>
      </ul>
    </div>
  </section>
</main>
</body>
</html>
```